LM Hair and Beauty flyer

Hello I have hairdressing salon called LM Hair and Beauty.I need flyer with double side pls.On front side I need this picture to be there and under the pisture our full address,tel number and email address( 48 Penwick rd E7 3QD 02084417396 media@lmhairandbeauty.co.uk). And under that shoud be written:Special offers
with 3 different discount squares at the bottom of the flyer.First visite 20% off,Second 15% off, thrd 10% off.At he other side of flyer should be following info:Ladies cut & blowdry with 3 different levels of stylist £45-£65,Gents cut £15-£36,Highlights from £45-£120,Express Blowdry £22-£35,Keratin tretmant £150,Manicure from £14,Pedicure from £25,Shellac from £28

Industry/Entity Type

Salon

```html
<!DOCTYPE html>
<html lang="en">
<head>
<meta charset="utf-8">
<title>LM Hair and Beauty – Flyer</title>
<link rel="stylesheet" href="https://fonts.googleapis.com/css2?family=Roboto+Condensed:wght@400;700&family=Courgette&family=Montserrat:wght@600&display=swap">
<style>
  :root {
    --backdrop: #ebe7e2;
    --pink: #e8118b;
    --pink-soft: #f06ab6;
    --mauve-top: #a14d86;
    --mauve-mid: #d49cc3;
    --mauve-low: #9e4c86;
    --teal: #1a9a98;
    --ink: #1c1418;
    --white: #ffffff;
    --pale: #d9d4d8;
    --photo-dark: #3c3236;
    --photo-mid: #8c8185;
    --photo-light: #cfc7c9;
  }
  * { margin: 0; padding: 0; box-sizing: border-box; }
  html, body {
    width: 1200px; height: 877px; overflow: hidden;
    background: var(--backdrop);
    font-family: "Roboto Condensed", "Arial Narrow", sans-serif;
  }
  .canvas { position: relative; width: 1200px; height: 877px; }

  .flyer { position: absolute; top: 48px; width: 547px; height: 774px; overflow: hidden; background: var(--white); }
  .flyer--front { left: 33px; }
  .flyer--back { left: 620px; }

  /* front */
  .team-photo {
    position: absolute; left: 0; top: 0; width: 547px; height: 600px;
    background: linear-gradient(180deg, var(--photo-light) 0%, var(--photo-mid) 35%, var(--photo-dark) 80%);
  }
  .front-band { position: absolute; left: 0; top: 450px; width: 547px; height: 190px; }
  .contact { position: absolute; left: 29px; top: 552px; color: var(--white); font-weight: 700; }
  .contact__line { font-size: 17px; line-height: 25px; }
  .contact__phone { display: flex; align-items: center; gap: 4px; font-size: 25px; letter-spacing: 1.5px; margin-top: 3px; }
  .contact__phone svg { width: 20px; height: 20px; }

  .brand-mark {
    position: absolute; width: 176px; height: 176px; border-radius: 50%;
    background: var(--teal);
    display: flex; align-items: center; justify-content: center; text-align: center;
    color: var(--white); font-weight: 700; font-size: 24px; line-height: 28px; padding: 24px;
  }
  .flyer--front .brand-mark { left: 326px; top: 449px; }
  .flyer--back .brand-mark { left: 340px; top: 461px; }

  .coupons { position: absolute; left: 4px; top: 637px; display: flex; gap: 5px; }
  .coupon {
    width: 176px; height: 135px; background: var(--white);
    border: 2px dashed var(--pink-soft); outline: 3px solid var(--white);
    text-align: center; padding-top: 4px;
  }
  .coupon__value { font-family: "Courgette", cursive; color: var(--pink); font-size: 52px; line-height: 58px; }
  .coupon__off { font-weight: 700; font-size: 34px; line-height: 34px; letter-spacing: 3px; color: var(--ink); }
  .coupon__visit { font-weight: 700; font-size: 20px; line-height: 28px; color: var(--ink); }

  /* back */
  .model-photo {
    position: absolute; left: 0; top: 0; width: 547px; height: 345px;
    background: radial-gradient(ellipse at 50% 55%, #c9a07d 0%, #a99a98 30%, var(--photo-light) 70%);
  }
  .price-panel {
    position: absolute; left: 0; top: 332px; width: 547px; height: 442px;
    background: linear-gradient(180deg, var(--mauve-top) 0%, var(--mauve-mid) 45%, var(--mauve-low) 100%);
  }
  .price-title {
    position: absolute; left: 0; width: 547px; top: 366px; text-align: center;
    color: var(--pink); font-weight: 700; font-size: 25px;
  }
  .price-list { position: absolute; left: 58px; top: 411px; list-style: none; }
  .price-list li {
    position: relative; padding-left: 13px; color: var(--ink);
    font-weight: 700; font-size: 22px; line-height: 31.5px;
  }
  .price-list li::before {
    content: ""; position: absolute; left: 0; top: 13px; width: 8px; height: 8px;
    border-radius: 50%; background: var(--pink);
  }
  .booking {
    position: absolute; left: 18px; top: 679px; width: 519px; height: 81px;
    border-radius: 12px; background: var(--pink); text-align: center; padding-top: 8px;
  }
  .booking__label { font-family: "Montserrat", sans-serif; font-weight: 600; font-size: 21px; letter-spacing: 3px; color: var(--ink); }
  .booking__phone {
    display: flex; justify-content: center; align-items: center; gap: 6px;
    font-family: "Montserrat", sans-serif; font-weight: 600; font-size: 30px; letter-spacing: 3px; color: var(--pale);
  }
  .booking__phone svg { width: 24px; height: 24px; }
</style>
</head>
<body>
<div class="canvas">

  <section class="flyer flyer--front">
    <div class="team-photo" role="img" aria-label="Black and white photo of the salon team posing together inside the salon"></div>
    <svg class="front-band" viewBox="0 0 547 190" preserveAspectRatio="none" aria-hidden="true">
      <path d="M0 35 Q180 95 547 40 L547 190 L0 190 Z" fill="var(--pink)"/>
    </svg>
    <div class="brand-mark">LM Hair and Beauty</div>
    <div class="contact">
      <p class="contact__line">48 Penwick Rd, E7 3QD</p>
      <p class="contact__line">media@lmhairandbeauty.co.uk</p>
      <p class="contact__phone">
        <svg viewBox="0 0 24 24" aria-hidden="true"><circle cx="12" cy="12" r="10.5" fill="none" stroke="var(--white)" stroke-width="2"/><path d="M9 6 L11 9 L9.5 10.5 Q10.5 13.5 13.5 14.5 L15 13 L18 15 L16.5 17.5 Q8 16 6.5 7.5 Z" fill="var(--white)"/></svg>
        02084417396
      </p>
    </div>
    <div class="coupons">
      <div class="coupon"><p class="coupon__value">20%</p><p class="coupon__off">OFF</p><p class="coupon__visit">Your First Visit</p></div>
      <div class="coupon"><p class="coupon__value">15%</p><p class="coupon__off">OFF</p><p class="coupon__visit">Your Second Visit</p></div>
      <div class="coupon"><p class="coupon__value">10%</p><p class="coupon__off">OFF</p><p class="coupon__visit">Your Third Visit</p></div>
    </div>
  </section>

  <section class="flyer flyer--back">
    <div class="model-photo" role="img" aria-label="Smiling woman with a blonde bob holding the price board, salon team faded behind her"></div>
    <div class="price-panel"></div>
    <h2 class="price-title">Our Latest Hair and Beauty Prices</h2>
    <ul class="price-list">
      <li>Three Level Women’s Cut &amp; Blowdry&nbsp; £45-£65</li>
      <li>Men’s Hair cut £15-£36</li>
      <li>Highlights from £45-£120</li>
      <li>Express Blowdry £22-£35</li>
      <li>Keratin treatment £150</li>
      <li>Manicure from £14</li>
      <li>Pedicure from £25</li>
      <li>Shellac Manicure from £28</li>
    </ul>
    <div class="brand-mark">LM Hair and Beauty</div>
    <div class="booking">
      <p class="booking__label">FOR APPOINTMENT CALL</p>
      <p class="booking__phone">
        <svg viewBox="0 0 24 24" aria-hidden="true"><circle cx="12" cy="12" r="10.5" fill="none" stroke="var(--pale)" stroke-width="2"/><path d="M9 6 L11 9 L9.5 10.5 Q10.5 13.5 13.5 14.5 L15 13 L18 15 L16.5 17.5 Q8 16 6.5 7.5 Z" fill="var(--pale)"/></svg>
        02084417396
      </p>
    </div>
  </section>

</div>
</body>
</html>
```